Orsabellitravel.com web design project + logo design

Hi,

We are a Russian online tour operator - tripwelder.com

We are looking to tranmsfer our domain to orsabellitravel.com. The website and logo need to be orsabelliesque - we are not looking to change our functionality, but we need to make the website much more attracitve to clients, much more wild looking but at the same time remaining a professional travel company.

The main concept of the website should be innovative travel (as orsabelli was an innovator). Alternatively, you could go down the artist route and go down the draw / design your own tour road.

On our website the customer is able to combine travel services (hotels, flights, Visa services, and soon chauffeur, car rental etc...) put it into their basket (the basket definitely has to look better than it is at the moment) and pay for it in one go by card.

We are also stressin our customer support with web chat, call centre etc... (call centre number at the top of the page)

We aim to provide an easy user experience, but we need to make it have some more style, so I will be waiting for what you guys can come up with.
Let me know if you have any questions - skype is: mrkolbuzov

It Company

• It is quite a simple task - to take the existing website tripwelder.com and orsabellisize it to create orsabellitravel.com, the functionality of the website will remain the same and there are not many pages in the website. Homepage, Checkout step1, Checkout step 2 (you can view both of these if you select a service) and the generic pages for T&C''s, Privacy policy etc...

IMPORTANT UPDATE

We are also looking at how the search results will look in the designs, (please do a search on our website for hotel / flight)

```html
<!DOCTYPE html>
<html lang="en">
<head>
<meta charset="utf-8">
<title>Orsabellitravel.com</title>
<link href="https://fonts.googleapis.com/css2?family=Open+Sans:wght@400;600;700&family=Sintony:wght@400;700&display=swap" rel="stylesheet">
<style>
:root{
  --sky:#a9d5ee;
  --white:#ffffff;
  --navy:#1c3d78;
  --blue:#2d9ee0;
  --blue-deep:#1682c6;
  --link:#1a7cc8;
  --panel:#d9edf8;
  --photo:#c4dde8;
  --footer:#e6f0f8;
  --text:#7b7b7b;
  --dark:#333333;
  --green:#2e8b2e;
  --brown:#4b2c25;
  --bar:#2f2f2f;
}
*{box-sizing:border-box;margin:0;padding:0}
html,body{width:1200px;height:2335px;overflow:hidden}
body{background:var(--sky);font-family:"Open Sans",Arial,sans-serif;color:var(--text);position:relative}
.page{position:absolute;left:109px;top:31px;width:982px;height:2267px;background:var(--white);border-radius:4px;overflow:hidden}
.abs{position:absolute}
a{color:inherit;text-decoration:none}
/* header */
.util-links{right:16px;top:12px;font-size:11.5px;color:var(--link);display:flex;gap:14px}
.brand{left:28px;top:40px;display:flex;align-items:center;gap:8px;font-family:"Sintony",sans-serif;font-weight:700;font-size:22px;color:var(--navy)}
.brand .dot{width:26px;height:26px;border-radius:50%;background:var(--blue)}
.welcome{left:370px;top:52px;width:200px;text-align:center;font-family:"Sintony",sans-serif;font-size:14px;color:#555}
.welcome .auth{color:var(--link);margin-top:4px}
.call{right:0;top:53px;width:207px;height:47px;background:var(--brown);color:#fff;font-family:"Sintony",sans-serif;font-weight:700;font-size:12.5px;text-align:center;line-height:16px;padding-top:7px;clip-path:polygon(14px 0,100% 0,100% 100%,14px 100%,0 50%)}
/* nav */
.nav{left:0;top:121px;width:982px;height:52px;background:linear-gradient(#45b2e8,var(--blue-deep))}
.nav-item{top:0;height:52px;line-height:52px;color:#fff;font-family:"Sintony",sans-serif;font-weight:700;font-size:11.5px;text-transform:uppercase}
.nav-home{left:20px;top:13px;width:73px;height:26px;background:#fff;color:#222;border-radius:3px;text-align:center;line-height:26px;font-family:"Sintony",sans-serif;font-weight:700;font-size:11.5px}
.nav-divider{left:736px;top:0;width:1px;height:52px;background:#0f6aa6}
.social{top:15px;width:22px;height:22px;border-radius:50%;background:#2b4f6f}
/* hero */
.hero{left:22px;top:198px;width:940px;height:350px;border-radius:8px;overflow:hidden;box-shadow:0 2px 5px rgba(0,0,0,.25)}
.hero-side{left:0;top:0;width:252px;height:350px;background:var(--panel)}
.badge{left:29px;top:18px;width:118px;height:118px;border-radius:50%;background:radial-gradient(circle at 40% 35%,#2f5ea8,#16336b);color:#fff;font-family:"Sintony",sans-serif;font-weight:700;font-size:14px;line-height:17px;text-align:center;padding-top:32px}
.badge-find{left:129px;top:66px;width:78px;height:78px;border-radius:50%;background:linear-gradient(#6fd2f0,#2aa6db);color:#fff;font-family:"Sintony",sans-serif;font-weight:700;font-size:13px;line-height:16px;padding:22px 0 0 18px}
.service{left:0;width:252px;height:71px;border-top:1px solid #b9dcef;padding:7px 16px}
.service h3{font-family:"Sintony",sans-serif;font-weight:400;font-size:16px;color:var(--dark);display:flex;align-items:center;gap:12px}
.service h3 i{display:inline-block;width:14px;height:14px;border-radius:50%;background:#fff;border:1px solid #ccc;position:relative}
.service h3 i:after{content:"";position:absolute;left:5px;top:3px;border-left:5px solid #555;border-top:3.5px solid transparent;border-bottom:3.5px solid transparent}
.service p{font-size:11.5px;line-height:15px;color:#888;margin-top:3px}
.hero-photo{left:252px;top:0;width:688px;height:350px;background:var(--photo)}
.dots{right:12px;bottom:8px;display:flex;gap:7px}
.dots span{width:17px;height:17px;border-radius:50%;background:#444;color:#fff;font-size:9px;text-align:center;line-height:17px}
.dots span.on{background:#1f6a2a}
.find-title{left:28px;top:576px;font-family:"Sintony",sans-serif;font-weight:400;font-size:16.5px;color:var(--dark);letter-spacing:.3px}
/* search */
.search{left:0;top:621px;width:982px;height:110px;background:linear-gradient(#48b5ea,var(--blue-deep))}
.select{height:26px;background:#fff;border-radius:4px;font-size:11px;color:#aaa;padding-left:14px;line-height:26px}
.select:after{content:"";position:absolute;right:4px;top:4px;width:18px;height:18px;border-radius:50%;background:#2aa0d6}
.select b{position:absolute;right:9px;top:10px;width:8px;height:8px;border-right:2px solid #fff;border-bottom:2px solid #fff;transform:rotate(45deg);z-index:1;margin-top:-3px}
.check{left:683px;font-size:10.5px;color:#fff;display:flex;align-items:center;gap:5px}
.check i{width:11px;height:11px;background:#fff;border:1px solid #999;display:inline-block;position:relative}
.check i.on:after{content:"";position:absolute;left:3px;top:0;width:3px;height:6px;border-right:2px solid #333;border-bottom:2px solid #333;transform:rotate(45deg)}
.avail{left:818px;top:32px;width:164px;height:46px;background:linear-gradient(#f4f8f4,#d8e5da);clip-path:polygon(16px 0,100% 0,100% 100%,16px 100%,0 50%);color:#2b6e2f;font-family:"Sintony",sans-serif;font-size:15px;line-height:46px;padding-left:30px}
/* content */
.content{left:43px;top:760px;width:906px}
.content section{margin-bottom:38px}
.content h2{font-family:"Sintony",sans-serif;font-weight:400;font-size:22px;color:var(--navy);margin-bottom:11px}
.content p{font-size:13.4px;line-height:22.8px;color:var(--text)}
.content ul{list-style:none;margin-top:9px}
.content li{font-size:12px;color:var(--green);line-height:30.3px;padding-left:20px;position:relative}
.content li:before{content:"";position:absolute;left:0;top:13px;width:5px;height:5px;border-radius:50%;background:var(--green)}
/* testimonials */
.strip{left:0;top:1774px;width:982px;height:207px;border-top:3px solid #e2e2e2}
.col{top:0;height:204px;padding:18px 0 0 22px}
.col+.col{border-left:3px solid #e2e2e2}
.col-title{height:33px;background:var(--bar);color:#fff;font-family:"Sintony",sans-serif;font-size:13px;line-height:33px;padding-left:34px;width:264px;position:relative}
.col-icon{position:absolute;left:-14px;top:-1px;width:36px;height:36px;border-radius:50%;background:#1e8fd3;border:3px solid #fff}
.col p{font-size:11.5px;line-height:19px;color:var(--dark);margin-top:12px;width:270px}
.col .who{font-size:11px;color:#777;line-height:17px}
.col .more{color:var(--link);font-size:11.5px;margin-top:6px}
.col ul{list-style:none;margin-top:14px;padding-left:6px}
.col li{font-size:11.5px;color:var(--dark);line-height:23px}
.col li:before{content:"›";margin-right:9px;color:#555}
/* footer */
.footer{left:0;top:1981px;width:982px;height:198px;background:var(--footer)}
.fcol{top:22px}
.fcol h4{font-family:"Sintony",sans-serif;font-weight:400;font-size:15.5px;color:var(--navy);margin-bottom:14px}
.fcol li{list-style:none;font-size:11.5px;color:#333;line-height:18px}
.fcol .fl{display:flex;align-items:center;gap:8px;line-height:26px}
.fcol .fl i{width:18px;height:18px;background:#6c9bd0;display:inline-block}
.base{left:0;top:2179px;width:982px;height:88px}
.base-brand{left:28px;top:35px;font-family:"Sintony",sans-serif;font-weight:700;font-size:20px;color:#444}
.legal{left:250px;top:25px;width:480px;text-align:center;font-size:11.5px;line-height:17px;color:#555}
.legal a{color:var(--link)}
.cards{right:20px;top:32px;display:flex;gap:4px}
.cards span{width:39px;height:22px;border-radius:3px;border:1px solid #ccc;background:#f3f3f3}
</style>
</head>
<body>
<div class="page">
  <nav class="abs util-links"><a href="#">Help</a><span>|</span><a href="#">My Account</a><span>|</span><a href="#">Customer Care</a></nav>
  <div class="abs brand"><span class="dot"></span>orsabellitravel.com</div>
  <div class="abs welcome">Welcome to Orsabelli Travels<div class="auth">Login | Register</div></div>
  <div class="abs call">YOU CALL, WE'RE THERE<br>(866-OTRAVEL)</div>

  <div class="abs nav">
    <div class="abs nav-home">HOME</div>
    <div class="abs nav-item" style="left:145px">Destinations</div>
    <div class="abs nav-item" style="left:301px">Activites</div>
    <div class="abs nav-item" style="left:432px">Trip Styles</div>
    <div class="abs nav-item" style="left:566px">Responsible Travel</div>
    <div class="abs nav-divider"></div>
    <div class="abs nav-item" style="left:756px">Follow us</div>
    <span class="abs social" style="left:851px"></span>
    <span class="abs social" style="left:885px"></span>
    <span class="abs social" style="left:922px"></span>
  </div>

  <div class="abs hero">
    <div class="abs hero-side">
      <div class="abs badge">USA's Biggest<br>Travel<br>Company</div>
      <div class="abs badge-find">Find<br>Here</div>
      <div class="abs service" style="top:138px"><h3>Visa Service <i></i></h3><p>Lorem Ipsum est simplement du faux texte employé .</p></div>
      <div class="abs service" style="top:209px"><h3>Flight Servive <i></i></h3><p>Lorem Ipsum est simplement du faux texte employé .</p></div>
      <div class="abs service" style="top:280px"><h3>Hotel Service <i></i></h3><p>Lorem Ipsum est simplement du faux texte employé .</p></div>
    </div>
    <div class="abs hero-photo" role="img" aria-label="Photo of a tropical beach with a turquoise lagoon, overwater bungalows and deck chairs on the sand"></div>
    <div class="abs dots"><span class="on">1</span><span>2</span><span>3</span><span>4</span></div>
  </div>

  <h1 class="abs find-title">FIND THE RIGHT PLACE FOR YOUR SUMMER HOLIDAY</h1>

  <form class="abs search">
    <div class="abs select" style="left:22px;top:20px;width:277px">Selec any 1<b></b></div>
    <div class="abs select" style="left:308px;top:20px;width:257px">Selec any 1<b></b></div>
    <div class="abs select" style="left:576px;top:20px;width:211px">Selec any 1<b></b></div>
    <div class="abs select" style="left:22px;top:64px;width:134px">Selec any 1<b></b></div>
    <div class="abs select" style="left:170px;top:64px;width:133px">Selec any 1<b></b></div>
    <div class="abs select" style="left:322px;top:64px;width:135px">Selec any 1<b></b></div>
    <div class="abs select" style="left:471px;top:64px;width:198px">Selec any 1<b></b></div>
    <div class="abs check" style="top:63px"><i></i>Обратно</div>
    <div class="abs check" style="top:80px"><i class="on"></i>В одну сторону</div>
    <div class="abs avail">View Availability</div>
  </form>

  <main class="abs content">
    <section>
      <h2>Visa Service</h2>
      <p>Lorem Ipsum est simplement du faux texte employé dans la sition et la misen page avant impression. Le Lorem Ipsum est le faux texte standard de l'imprimerie depuis les années 1500, quand un peintre anonyme assembla ensemble des morceaux de texte pour réaliser un livre spécimen de polices de texte. Il n'a pas fait que survivre cinq siècles, mais s'est aussi adapté à la bureautique informatique, sans que son contenu n'en soit modifié. Il a été popularisé dans les années 1960 grâce à la vente de feuilles Lettrafix contenant des passages du Lorem Ipsum, et, plus récemment, par son inclusion dans des applications de mise en page de texte, comme Quill Layout.</p>
      <ul><li>Ensemble morceaux quand un peintre anonyme assembla</li><li>Peintre anonyme assembla ensemble des morceaux quand un</li><li>Quand peintre anonyme assembla ensemble des morceaux</li><li>Anony assembla ensemble des morceaux quand un peintre</li></ul>
    </section>
    <section>
      <h2>Flight Service</h2>
      <p>Lorem Ipsum est simplement du faux texte employé dans la sition et la misen page avant impression. Le Lorem Ipsum est le faux texte standard de l'imprimerie depuis les années 1500, quand un peintre anonyme assembla ensemble des morceaux de texte pour réaliser un livre spécimen de polices de texte. Il n'a pas fait que survivre cinq siècles, mais s'est aussi adapté à la bureautique informatique, sans que son contenu n'en soit modifié. Il a été popularisé dans les années 1960</p>
      <ul><li>Ensemble morceaux quand un peintre anonyme assembla</li><li>Peintre anonyme assembla ensemble des morceaux quand un</li></ul>
    </section>
    <section>
      <h2>Hotelling Service</h2>
      <p>Lorem Ipsum est simplement du faux texte employé dans la sition et la misen page avant impression. Le Lorem Ipsum est le faux texte standard de l'imprimerie depuis les années 1500, quand un peintre anonyme assembla ensemble des morceaux de texte pour réaliser un livre spécimen de polices de texte.</p>
      <ul><li>Ensemble morceaux quand un peintre anonyme assembla</li><li>Peintre anonyme assembla ensemble des morceaux quand un</li></ul>
    </section>
    <section>
      <h2>Car Rental Service</h2>
      <p>Lorem Ipsum est simplement du faux texte employé dans la sition et la misen page avant impression. Le Lorem Ipsum est le faux texte standard de l'imprimerie depuis les années 1500, quand un peintre anonyme assembla ensemble des morceaux de texte pour réaliser un livre spécimen de polices de texte.</p>
      <ul><li>Ensemble morceaux quand un peintre anonyme assembla</li><li>Peintre anonyme assembla ensemble des morceaux quand un</li></ul>
    </section>
  </main>

  <div class="abs strip">
    <div class="abs col" style="left:0;width:327px">
      <div class="col-title"><span class="col-icon"></span>Genuine Customer Comments</div>
      <p>Lorem Ipsum est simplement du faux texte employé dans la sition et la misen page avant impression. Le Lorem Ipsum est le faux texte standard de l'imprimerie depuis les années 1500, quand un .</p>
      <div class="who">K Marlowe, London</div>
      <div class="more">View More Comments &nbsp;›</div>
    </div>
    <div class="abs col" style="left:327px;width:327px">
      <div class="col-title"><span class="col-icon"></span>Comments From Happy Customer</div>
      <p>Lorem Ipsum est simplement du faux texte employé dans la sition et la misen page avant impression. Le Lorem Ipsum est le faux texte standard de l'imprimerie depuis les années 1500, quand un .</p>
      <div class="who">R Thistle, London</div>
      <div class="more">View More Comments &nbsp;›</div>
    </div>
    <div class="abs col" style="left:654px;width:328px">
      <div class="col-title"><span class="col-icon"></span>More About Our Services</div>
      <ul><li>Visa Service</li><li>Flights Service</li><li>Hoteling Service</li><li>Car Rental Service</li></ul>
      <div class="more" style="margin-top:14px;padding-left:4px">View All Services &nbsp;›</div>
    </div>
  </div>

  <footer class="abs footer">
    <div class="abs fcol" style="left:23px"><h4>Customer Services</h4><ul><li>Europe</li><li>North America</li><li>South America</li><li>Africa</li><li>Asia</li></ul></div>
    <div class="abs fcol" style="left:227px"><h4>Customer info</h4><ul><li>Home</li><li>Activites</li><li>Trip Styles</li><li>Responsible Travel.</li></ul></div>
    <div class="abs fcol" style="left:406px"><h4>Our guarantees</h4><ul><li>Money back guarantee</li><li>Low price guarantee</li></ul></div>
    <div class="abs fcol" style="left:616px"><h4>Payment</h4><ul><li>Payment methods we accept</li><li>Open a business account</li><li>Schools and local authorities</li></ul></div>
    <div class="abs fcol" style="left:818px"><h4>Follow Us:</h4><ul><li class="fl"><i></i>Follow on Facelink</li><li class="fl"><i></i>Follow on Chirper</li><li class="fl"><i></i>Follow on Linkwork</li></ul></div>
  </footer>

  <div class="abs base">
    <div class="abs base-brand">orsabellitravel.com</div>
    <div class="abs legal">1-800-555-0147 | Copyright © 2013 <a href="#">orsabellitravel.com</a> | <a href="#">Terms of Use</a> | <a href="#">Advice Center</a><br>Company No: ABC1234 VAT Registration No: 123 456 789 Data Protection<br>Reg: A898764031</div>
    <div class="abs cards"><span></span><span></span><span></span><span></span></div>
  </div>
</div>
</body>
</html>
```